Web Design Project

i'm looking for a sleek modern design i can use for a web site that deals with.
Intelligent Data Capture
Accounts Payable Solutions for faster processing based on our scanning solution.
ultimately we are a intelligent scanning software.

here is a great website, that does exactly what we do, and we like to have most of their services and products.

so something in this idea would be great.
www.varnol.com

so i guess i want a good landing/home page which is smartly designed so users will be inclined to leave their information.

and then information pages.

also i dont need any cms for you to include, i only need you to hook the html hooks for RANK Kettle as i already have a CMS and need it to hook in to that, i am including links to that cheat sheet.
so it is easier when included as you create the Theme.

http://www.rankkettle.com/how-to-create-website-template.html
http://www.rankkettle.com/cheat-sheet.html
Updates

Hi Guys sorry for the long pause in design, but here is where we stand.

what ever design i choose, i need that designer to customize a few things for me based on design that was designed.
and i will need designer to match that them to work with RANK Kettle
here is the cheat sheet for the hooks that we need to match and make it work.
if you have any questions let me know.

otherwise i look forward to working with you. and good luck.

Target Market(s)

CFO's AP Managers, mostly ppl who are not Tech freindly

Industry/Entity Type

Software

Requirements
Must have
• i need on home page, the rotating banner should have 1 ability to place clipvane links to show videos, and also ability to add buttons on these rotating banners that will allow forms to pop up take to another page.

```html
<!DOCTYPE html>
<html lang="en">
<head>
<meta charset="utf-8">
<title>Intelligent Data Capture for Accounts Payable</title>
<link rel="stylesheet" href="https://fonts.googleapis.com/css2?family=Arimo:ital,wght@0,400;0,700;1,700&display=swap">
<style>
  :root {
    --bg: #121212;
    --bg-stripe: #1a1a1a;
    --white: #ffffff;
    --text-soft: #dcdcdc;
    --grey: #8a8a8a;
    --grey-dark: #5e5e5e;
    --nav-text: #9a9a9a;
    --lime: #7ab51d;
    --lime-link: #9ddc2a;
    --rule: #363636;
    --panel-top: #2a2a2a;
    --panel-bottom: #171717;
    --panel-edge: #333333;
  }
  * { box-sizing: border-box; margin: 0; padding: 0; }
  html, body { width: 1200px; height: 1112px; overflow: hidden; }
  body {
    position: relative;
    font-family: "Arimo", Arial, sans-serif;
    color: var(--text-soft);
    background-color: var(--bg);
    background-image: repeating-linear-gradient(to bottom, var(--bg) 0 2px, var(--bg-stripe) 2px 3px);
  }
  a { text-decoration: none; color: inherit; }

  .site-title {
    position: absolute; left: 113px; top: 43px;
    font-size: 26px; font-weight: 400; letter-spacing: 1.5px; color: var(--white);
    -webkit-text-stroke: 0.4px var(--white);
  }
  .site-tagline {
    position: absolute; left: 114px; top: 74px;
    font-size: 15px; font-style: italic; font-weight: 700; color: var(--grey-dark);
  }
  .account-links {
    position: absolute; left: 989px; top: 43px;
    font-size: 12px; color: #bdbdbd;
  }

  .main-nav {
    position: absolute; left: 47px; top: 159px; width: 1106px; height: 68px;
    border-radius: 10px; border: 1px solid var(--panel-edge);
    background: linear-gradient(to bottom, var(--panel-top), var(--panel-bottom));
  }
  .main-nav a {
    position: absolute; top: 25px;
    font-size: 16px; font-weight: 700; color: var(--nav-text); letter-spacing: 0.3px;
  }
  .main-nav a.is-active { color: var(--lime); }

  .hero-media {
    position: absolute; left: 144px; top: 276px; width: 353px; height: 277px;
    background: linear-gradient(to bottom, #2c2c2c 0%, #1a1a1a 62%, #b9b9b9 63%, #8a8a8a 100%);
    border-radius: 10px 10px 4px 4px;
  }
  .hero-title {
    position: absolute; left: 662px; top: 266px;
    font-size: 90px; font-weight: 700; color: var(--lime); line-height: 1;
  }
  .hero-subtitle {
    position: absolute; left: 669px; top: 349px;
    font-size: 59px; font-weight: 700; font-style: italic; color: var(--grey); line-height: 1;
  }
  .hero-button {
    position: absolute; left: 666px; top: 472px; width: 270px; height: 64px;
    border: 1px solid var(--panel-edge); border-radius: 4px;
    background: linear-gradient(to bottom, var(--panel-top), var(--panel-bottom));
    font-size: 42px; font-weight: 700; color: var(--white);
    display: flex; align-items: center; justify-content: center;
  }

  .video-controls { position: absolute; left: 47px; top: 582px; }
  .video-time {
    position: absolute; left: 426px; top: 593px;
    font-size: 10px; color: var(--text-soft);
  }

  .info-column { position: absolute; top: 664px; }
  .info-column h2 {
    font-size: 21px; font-weight: 400; color: var(--text-soft);
    padding-bottom: 9px; border-bottom: 1px solid var(--rule);
  }
  .column-links { left: 48px; width: 305px; }
  .column-links li {
    list-style: none; height: 36.5px; line-height: 35px;
    font-size: 14px; color: var(--lime-link); border-bottom: 1px solid var(--rule);
  }
  .column-links li:last-child { border-bottom: none; }
  .column-articles { left: 394px; width: 388px; }
  .column-articles li {
    list-style: none; padding: 12px 0 13px;
    font-size: 13px; line-height: 15.5px; color: var(--lime-link);
    border-bottom: 1px solid var(--rule);
  }
  .column-articles li:last-child { border-bottom: none; }
  .column-about { left: 825px; width: 328px; }
  .column-about p.about-text {
    padding: 9px 0 10px; font-size: 13.5px; line-height: 20px; color: var(--text-soft);
    border-bottom: 1px solid var(--rule);
  }
  .column-about .about-link {
    display: block; padding: 9px 0 10px; font-size: 14px; color: var(--lime-link);
    border-bottom: 1px solid var(--rule);
  }
  .column-about .copyright { padding-top: 9px; font-size: 14px; color: var(--text-soft); }
</style>
</head>
<body>
  <header>
    <h1 class="site-title">INTELLIGENT DATA CAPTURE</h1>
    <p class="site-tagline">for Accounts Payable</p>
    <p class="account-links"><a href="#">Login</a> or <a href="#">Register</a></p>
  </header>

  <nav class="main-nav">
    <a class="is-active" href="#" style="left:66px">HOME</a>
    <a href="#" style="left:186px">SEMPER</a>
    <a href="#" style="left:325px">NUSQUAM</a>
    <a href="#" style="left:479px">LEGERE</a>
    <a href="#" style="left:617px">ELECTRAM</a>
    <a href="#" style="left:779px">OMNIUS REBUS</a>
    <a href="#" style="left:962px">CONTACT</a>
  </nav>

  <section class="hero">
    <div class="hero-media" role="img" aria-label="Laptop showing the featured product video"></div>
    <h2 class="hero-title">URBANUS</h2>
    <p class="hero-subtitle">OBLIQUE</p>
    <a class="hero-button" href="#">GO</a>

    <svg class="video-controls" width="560" height="32" viewBox="0 0 560 32" aria-label="Video player controls">
      <circle cx="15" cy="16" r="12.5" fill="#1c1c1c" stroke="#9a9a9a" stroke-width="2"/>
      <rect x="10.5" y="10" width="3" height="12" fill="#e6e6e6"/>
      <rect x="16.5" y="10" width="3" height="12" fill="#e6e6e6"/>
      <rect x="37" y="12" width="334" height="8" rx="4" fill="#1e1e1e"/>
      <rect x="37" y="12" width="267" height="8" rx="4" fill="#8a8a8a"/>
      <rect x="37" y="12" width="182" height="8" rx="4" fill="#7ab51d"/>
      <circle cx="219" cy="16" r="7" fill="#2a2a2a" stroke="#ffffff" stroke-width="2"/>
      <path d="M418 12 h5 l7 -5 v18 l-7 -5 h-5 z" fill="#2e2e2e"/>
      <rect x="445" y="13" width="68" height="6" rx="3" fill="#cfcfcf"/>
      <rect x="445" y="13" width="44" height="6" rx="3" fill="#7ab51d"/>
      <rect x="486" y="9" width="4" height="14" rx="1" fill="#ffffff"/>
      <g stroke="#9a9a9a" stroke-width="1.8" fill="none">
        <path d="M527 10 l5 5 M527 10 h4 M527 10 v4"/>
        <path d="M543 10 l-5 5 M543 10 h-4 M543 10 v4"/>
        <path d="M527 24 l5 -5 M527 24 h4 M527 24 v-4"/>
        <path d="M543 24 l-5 -5 M543 24 h-4 M543 24 v-4"/>
      </g>
    </svg>
    <span class="video-time">04:25</span>
  </section>

  <section class="info-column column-links">
    <h2>Oblique Elaboraret</h2>
    <ul>
      <li>Reformidans Iuvaret</li>
      <li>Consequuntur</li>
      <li>Ullamcorper Essent</li>
      <li>Gloriatur</li>
      <li>Primis Scriptorem</li>
      <li>Nulla</li>
      <li>Reformidans</li>
      <li>Consequuntur</li>
      <li>Gloriatur Dicam</li>
    </ul>
  </section>

  <section class="info-column column-articles">
    <h2>Legimus Philosophia</h2>
    <ul>
      <li>Laboramus prodesset instructior: Ex duo, eum at minim accusam</li>
      <li>Ei usu: Qualisque Suscipiantur</li>
      <li>Cu ferri ornatus consequat qui, ea case modus perpetua nam, qui no agam docendi noluisse</li>
      <li>Eum hendrerit consequat: no sea sumo</li>
      <li>Ex duo, eum at minim accusam. Ei usu qualisque suscipiantur, cu his veniam honestatis. Cu ferri ornatus consequat qui, ea case modus perpetua nam</li>
      <li>Laboramus prodesset instructior: Ex duo, eum at minim accusam</li>
      <li>Ei usu: Qualisque Suscipiantur</li>
    </ul>
  </section>

  <section class="info-column column-about">
    <h2>Modus</h2>
    <p class="about-text">Modo scriptorem an per, modus consul partem duo cu, falli saperet mandamus in vel. Ius insolens mandamus necessitatibus ad, ei quo percipit urbanitas intellegebat. Ea eam eros utroque vulputate, harum tation munere ea mea. Usu id postea mollis quaerendum, has oratio utroque</p>
    <a class="about-link" href="#">Ei usu: Qualisque Suscipiantur</a>
    <p class="copyright">Copyright © Company Name</p>
  </section>
</body>
</html>
```